Center for Cellular Datawork wordpress design

We need a wordpress design for the new Center for Cellular Datawork at the Marrowfield University. We are a research institute focused on medical and biological research involving big data and informatics. The website has to be eyecatching and appropriate for an academic context, with easily updated content.

Press release here: http://www.mfhs.marrowfield-u.edu/news/News_Releases/2013/02/cellular/

We would prefer to use images from our research labs over stock art, but feel free to use placeholders for now. Please contact me if there are specific types of images you need.

Target Market(s)

Tech-savvy academics, faculty, students, general laypeople

Industry/Entity Type

Medical

Requirements
Must have
• Use existing logo (attached, other versions available upon request)

Sections for:
Mission statement (draft version attached)
Educational Programs: there is only one at the moment, but we will need the option to add more
Faculty members/resident staff (contact database); webform to apply to join
Events calendar/list
Emphasis on search engine optimization
Nice to have
• News/publication tabs for the front page (similar to those on http://www.ovrek.marrowfield-u.edu/)

It would be helpful if you could use the Marrowfield color palette: http://www.marrowfield-u.edu/webservices/styleguide/color.html

```html
<!DOCTYPE html>
<html lang="en">
<head>
<meta charset="utf-8">
<title>Center for Cellular Datawork</title>
<link href="https://fonts.googleapis.com/css2?family=Arimo:wght@400;700&family=PT+Sans:wght@400;700&display=swap" rel="stylesheet">
<style>
:root{
  --red:#b00d12;
  --red-soft:#e9b3b3;
  --navy:#1f2f6b;
  --ink:#333333;
  --muted:#888888;
  --line:#e3e3e3;
  --band:#f4f4f4;
  --dark:#2e2e2e;
  --black:#111111;
  --white:#ffffff;
}
*{box-sizing:border-box;margin:0;padding:0}
html,body{width:792px;height:1200px;overflow:hidden;background:var(--white)}
body{position:relative;font-family:"Arimo",Arial,sans-serif;color:var(--ink)}
.abs{position:absolute}
.nav-font{font-family:"PT Sans",Arial,sans-serif}

.topbar{left:0;top:0;width:792px;height:18px;background:#f7f7f7;border-bottom:1px solid #eee}
.topbar .login{left:705px;top:5px;font-size:7px;color:var(--muted)}
.topbar .login::after{content:"⌄";margin-left:8px}

.header{left:0;top:18px;width:792px;height:50px;border-bottom:1px solid var(--line)}
.brand{left:50px;top:7px;display:flex;align-items:center;gap:6px}
.brand-mark{width:28px;height:28px;background:var(--navy)}
.brand-name{font-family:"PT Sans",Arial,sans-serif;font-size:15px;line-height:16px;color:var(--navy);width:190px}
.nav{left:456px;top:20px;display:flex;gap:7px;font-size:7.5px;color:#666}
.nav .active{color:var(--ink);border-bottom:2px solid var(--red);padding-bottom:6px}
.search-btn{left:720px;top:15px;width:16px;height:16px;background:#f0f0f0}

.hero{left:0;top:68px;width:792px;height:274px;background:linear-gradient(120deg,#f6e3e3 0%,#ffffff 35%,#f3f3f3 60%,#f1dede 100%);overflow:hidden}
.hero-photo{left:388px;top:0;width:404px;height:274px;background:linear-gradient(135deg,#d9464a 0%,#eef0f2 35%,#c7ced4 60%,#cf3036 100%)}
.hero-quote{left:60px;top:64px;width:326px;text-align:center;font-size:24.5px;line-height:29px;color:#222;letter-spacing:.3px}
.hero-quote strong{font-weight:700}
.hero-btn{left:190px;top:188px;width:60px;height:22px;background:#2a2a2a;color:#fff;border-radius:11px;font-family:"PT Sans",Arial,sans-serif;font-size:7.5px;text-align:center;line-height:22px}
.hero-arrow{top:125px;font-size:13px;color:#111}

.feature{top:360px;width:170px;text-align:center}
.feature h3{font-weight:400;font-size:9.5px;margin-top:10px}
.feature p{font-size:7px;line-height:12px;margin-top:18px;height:36px;padding:0 20px}
.feature .more{font-size:7.5px;color:var(--muted);margin-top:11px;font-family:"PT Sans",Arial,sans-serif}
.feature .more.hot{color:var(--red)}
.feature .more::after{content:" ›";color:var(--red);font-weight:700}

.band{left:0;top:585px;width:792px;height:55px;background:var(--band);border-top:1px solid var(--line);border-bottom:1px solid var(--line)}
.band h2{position:absolute;left:55px;top:17px;font-weight:400;font-size:15.5px;color:#333}
.pill{position:absolute;left:678px;top:18px;width:60px;height:18px;border-radius:9px;background:var(--red);color:#fff;font-family:"PT Sans",Arial,sans-serif;font-size:6.5px;text-align:center;line-height:18px}

.section-title{font-family:"PT Sans",Arial,sans-serif;font-size:10px;color:#222;padding-bottom:5px;border-bottom:1px solid #333}
.card{top:700px;width:158px}
.card-img{width:158px;height:120px}
.card h4{font-family:"PT Sans",Arial,sans-serif;font-weight:400;font-size:9px;margin-top:10px}
.card p{font-family:"PT Sans",Arial,sans-serif;font-size:7.5px;line-height:14px;margin-top:8px;color:#444;padding-right:10px}
.card .meta{margin-top:20px;padding-bottom:9px;border-bottom:1px solid var(--line);display:flex;justify-content:space-between;align-items:center;font-size:7px;color:var(--muted)}
.meta .stats{display:flex;align-items:center;gap:4px}

.accordion{left:405px;top:702px;width:157px}
.accordion div{height:29px;border:1px solid var(--line);margin-top:-1px;font-family:"PT Sans",Arial,sans-serif;font-size:7.5px;padding:10px 9px;position:relative}
.accordion div::after{content:"+";position:absolute;right:9px;top:7px;font-weight:700;font-size:10px}

.bars{left:580px;top:701px;width:157px}
.bar{height:24px;background:#f3f3f3;margin-bottom:6px}
.bar span{position:relative;display:block;height:24px;background:var(--red);color:#fff;font-size:6.5px;font-weight:700;line-height:24px;padding-left:10px}
.bar.striped span{background:repeating-linear-gradient(135deg,var(--red) 0 6px,#c4262b 6px 12px)}
.bar em{font-style:normal;position:absolute;right:10px;top:0;color:#fff}

.footer{left:0;top:964px;width:792px;height:206px;background:var(--dark);color:#ccc}
.footer-bottom{left:0;top:1170px;width:792px;height:30px;background:var(--black)}
.ftitle{position:absolute;left:0;top:0;font-size:6.5px;line-height:9px;color:#eee;padding-bottom:2px;border-bottom:1px solid #aaa;white-space:nowrap}
.fcontact{left:56px;top:25px;width:200px;height:160px;font-size:6px;line-height:9.5px}
.fcontact .body{position:absolute;left:0;top:20px;width:200px}
.fcontact a{color:var(--red)}
.frecent{left:285px;top:25px;width:215px;height:160px}
.frecent ul{position:absolute;left:0;top:22px;width:215px;list-style:none;border:1px solid #444}
.frecent li{height:22px;border-bottom:1px solid #444;font-size:7px;color:var(--red);padding:7px 0 0 8px}
.frecent li::before{content:"› ";color:#777}
.fevents{left:520px;top:25px;width:123px;height:160px}
.cal{position:absolute;left:0;top:20px;width:123px;background:#ddd}
.cal-head{background:#333;color:#eee;height:17px;display:flex;justify-content:space-between;align-items:center;padding:0 6px;font-size:10px}
.cal-grid{display:grid;grid-template-columns:repeat(7,1fr);background:#fff}
.cal-grid span{height:17px;border:1px solid #bbb;background:#d6d6d6;color:#222;font-size:8.5px;text-align:center;line-height:15px}
.cal-grid .dow{height:10px;line-height:10px;font-size:5px;background:#fff;border:none;font-weight:700}
.cal-grid .off{color:#777;background:#cfcfcf}
.cal-grid .today{outline:2px solid #5aa4c8;outline-offset:-3px;background:#eee}
</style>
</head>
<body>

<div class="abs topbar"><span class="abs login nav-font">Login</span></div>

<header class="abs header">
  <div class="abs brand"><span class="brand-mark"></span><span class="brand-name">Center for Cellular Datawork</span></div>
  <nav class="abs nav nav-font">
    <span class="active">Home</span><span>Mission Statement</span><span>Educational Programs</span><span>Events</span><span>News</span><span>Contact</span>
  </nav>
  <span class="abs search-btn"></span>
</header>

<section class="abs hero">
  <div class="abs hero-photo" role="img" aria-label="Close-up photograph of a molecular model with red atoms and dark bonds"></div>
  <div class="abs hero-quote">“TRAINING THE NEXT GENERATION OF <strong>PHYSICIAN-SCIENTISTS</strong>”</div>
  <div class="abs hero-btn">Tell me more</div>
  <span class="abs hero-arrow" style="left:35px">‹</span>
  <span class="abs hero-arrow" style="left:750px">›</span>
</section>

<div class="abs feature" style="left:49px">
  <svg width="88" height="88" viewBox="0 0 88 88"><circle cx="44" cy="44" r="39" fill="none" stroke="var(--red-soft)" stroke-width="7"/><circle cx="44" cy="44" r="39" fill="none" stroke="var(--red)" stroke-width="7" stroke-dasharray="196 245" transform="rotate(-90 44 44)" stroke-dashoffset="-49"/><rect x="40" y="38" width="8" height="12" rx="1" fill="none" stroke="#222" stroke-width="1.5"/></svg>
  <h3>Responsive Design</h3>
  <p>This design is completely responsive, meaning it will look great on mobile devices!</p>
  <div class="more hot">Find out more</div>
</div>
<div class="abs feature" style="left:224px">
  <svg width="88" height="88" viewBox="0 0 88 88"><circle cx="44" cy="44" r="39" fill="none" stroke="var(--red-soft)" stroke-width="7"/><circle cx="44" cy="44" r="39" fill="none" stroke="var(--red)" stroke-width="7" stroke-dasharray="122 245" transform="rotate(-90 44 44)"/><path d="M37 51 l2-6 9-9 4 4-9 9z" fill="#222"/></svg>
  <h3>Graphs</h3>
  <p>These animated circles relate to data and accompanying data. You might choose to showcase research findings in this areas.</p>
  <div class="more">Find out more</div>
</div>
<div class="abs feature" style="left:399px">
  <svg width="88" height="88" viewBox="0 0 88 88"><circle cx="44" cy="44" r="39" fill="none" stroke="var(--red-soft)" stroke-width="7"/><circle cx="44" cy="44" r="39" fill="none" stroke="var(--red)" stroke-width="7" stroke-dasharray="150 245" transform="rotate(-90 44 44)"/><text x="44" y="51" text-anchor="middle" font-family="Georgia,serif" font-weight="700" font-size="19" fill="#222">A</text></svg>
  <h3>Typefaces</h3>
  <p>This theme will use your corporate fonts Arial and Georgia.</p>
  <div class="more">Find out more</div>
</div>
<div class="abs feature" style="left:573px">
  <svg width="88" height="88" viewBox="0 0 88 88"><circle cx="44" cy="44" r="39" fill="none" stroke="var(--red-soft)" stroke-width="7"/><circle cx="44" cy="44" r="39" fill="none" stroke="var(--red)" stroke-width="7" stroke-dasharray="225 245" transform="rotate(-90 44 44)" stroke-dashoffset="-20"/><ellipse cx="44" cy="44" rx="8" ry="5" fill="#222"/><circle cx="44" cy="44" r="2.5" fill="#fff"/></svg>
  <h3>Search</h3>
  <p>Users can search for content at any time using the Search panel at top right.</p>
  <div class="more">Find out more</div>
</div>

<section class="abs band">
  <h2>Lastest Grant or other headline activity or area of interest.</h2>
  <span class="pill">Take the tour ›</span>
</section>

<div class="abs section-title" style="left:56px;top:673px">Latest articles / Educational Programmes</div>
<div class="abs" style="left:371px;top:675px;font-size:11px;font-weight:700">‹ ›</div>

<article class="abs card" style="left:55px">
  <div class="card-img" role="img" aria-label="Photograph of a modern glass office interior" style="background:linear-gradient(160deg,#3f6a8c,#a9c3d6 55%,#d8dde0)"></div>
  <h4>Page Builder Post 1</h4>
  <p>Lorem ipsum dolor sit amet, consectetur adipiscing elit. Etiam aliquam massa quis mauris sollicitudin commodo...</p>
  <div class="meta"><span>March 12, 2013</span><span class="stats"><svg width="7" height="6" viewBox="0 0 7 6"><path d="M0 0h7v4H3L1 6V4H0z" fill="#999"/></svg>7 &nbsp;<svg width="7" height="6" viewBox="0 0 7 6"><path d="M3.5 6 0 2.5A1.6 1.6 0 0 1 3.5 1 1.6 1.6 0 0 1 7 2.5z" fill="#999"/></svg>136</span></div>
</article>
<article class="abs card" style="left:229px">
  <div class="card-img" role="img" aria-label="Photograph of two researchers working in a laboratory" style="background:linear-gradient(150deg,#e8ecef,#c9d3da 50%,#eef1f3)"></div>
  <h4>Standard Post No Sidebar</h4>
  <p>Lorem ipsum dolor sit amet, consectetur adipiscing elit. Etiam aliquam massa quis mauris sollicitudin commodo...</p>
  <div class="meta"><span>November 2, 2012</span><span class="stats"><svg width="7" height="6" viewBox="0 0 7 6"><path d="M0 0h7v4H3L1 6V4H0z" fill="#999"/></svg>4 &nbsp;<svg width="7" height="6" viewBox="0 0 7 6"><path d="M3.5 6 0 2.5A1.6 1.6 0 0 1 3.5 1 1.6 1.6 0 0 1 7 2.5z" fill="#999"/></svg>134</span></div>
</article>

<div class="abs section-title" style="left:405px;top:673px">More about us</div>
<div class="abs accordion">
  <div>Who we are</div><div>What we do</div><div>Why we do it</div><div>Where we do it</div>
</div>

<div class="abs section-title" style="left:580px;top:673px">Our Capabilities</div>
<div class="abs bars">
  <div class="bar"><span style="width:118px">These bar charts can be used</span></div>
  <div class="bar striped"><span style="width:150px">For a range of information<em>95%</em></span></div>
  <div class="bar"><span style="width:134px">Such as areas of study<em>85%</em></span></div>
  <div class="bar"><span style="width:126px">Or Project Completeness<em>80%</em></span></div>
  <div class="bar"><span style="width:94px">Or Stats<em>60%</em></span></div>
  <div class="bar"><span style="width:78px">On Anything<em style="right:2px">50%</em></span></div>
</div>

<footer class="abs footer">
  <div class="abs fcontact">
    <span class="ftitle">CONTACT US</span>
    <div class="body">
      <p>Lorem ipsum dolor sit amet, consectetuer adipiscing elit. Nam cursus. Morbi ut mi. Nullam enim leo, egestas id, condimentum at, laoreet mattis, massa. Sed eleifend nonummy diam. Praesent mauris ante, elementum et, bibendum at, posuere sit amet, nibh. Duis tincidunt lectus quis dui viverra vestibulum.</p>
      <p style="margin-top:6px">Insert Street address here<br>City, State<br>United States</p>
      <p style="margin-top:6px">P: &nbsp;555-014-2560<br>F: &nbsp;555-014-2562</p>
      <p style="margin-top:6px">E: <a>info@marrowfield-cd.org</a></p>
    </div>
  </div>
  <div class="abs frecent">
    <span class="ftitle">RECENT ARTICLES</span>
    <ul><li>Page Builder Post 1</li><li>Standard Post No Sidebar</li><li>Double Sidebar Post</li><li>Gallery Post No Sidebar</li><li>Left Sidebar Post</li></ul>
  </div>
  <div class="abs fevents">
    <span class="ftitle">EVENTS</span>
    <div class="cal">
      <div class="cal-head"><span>◀</span><span>March &nbsp;2013</span><span>▶</span></div>
      <div class="cal-grid">
        <span class="dow">MON</span><span class="dow">TUE</span><span class="dow">WED</span><span class="dow">THU</span><span class="dow">FRI</span><span class="dow">SAT</span><span class="dow">SUN</span>
        <span class="off">25</span><span class="off">26</span><span class="off">27</span><span class="off">28</span><span>1</span><span>2</span><span>3</span>
        <span>4</span><span>5</span><span>6</span><span>7</span><span>8</span><span>9</span><span>10</span>
        <span>11</span><span>12</span><span>13</span><span>14</span><span>15</span><span>16</span><span>17</span>
        <span>18</span><span>19</span><span class="today">20</span><span>21</span><span>22</span><span>23</span><span>24</span>
        <span>25</span><span>26</span><span>27</span><span>28</span><span>29</span><span>30</span><span>31</span>
        <span class="off">1</span><span class="off">2</span><span class="off">3</span><span class="off">4</span><span class="off">5</span><span class="off">6</span><span class="off">7</span>
      </div>
    </div>
  </div>
</footer>
<div class="abs footer-bottom"></div>

</body>
</html>
```